Anchorwell Giving - New Website Designed

I need a site that looks like this http://www.lumenhavenfund.org for boat donations. So please replace the cars with boats.

```html
<!DOCTYPE html>
<html lang="en">
<head>
<meta charset="utf-8">
<title>Anchorwell Giving – Donate Your Boat</title>
<link rel="stylesheet" href="https://fonts.googleapis.com/css2?family=Oswald:wght@400;500&family=Open+Sans:wght@400;600&display=swap">
<style>
:root{
  --navy:#2e3f9b;
  --navy-dark:#24327f;
  --orange:#f26b4a;
  --orange-btn:#f36f4c;
  --grey-bg:#f2f3f5;
  --icon-fill:#dfe2ec;
  --text:#333;
  --muted:#888;
  --white:#fff;
}
*{margin:0;padding:0;box-sizing:border-box}
html,body{width:1200px;height:2287px;overflow:hidden}
body{font-family:"Open Sans",sans-serif;color:var(--text);background:var(--white);position:relative}
.section{position:absolute;left:0;width:1200px}
.heading{font-family:"Oswald",sans-serif;font-weight:400;text-transform:uppercase}
.accent{color:var(--orange)}
.btn{position:absolute;background:var(--orange-btn);color:var(--white);font-family:"Oswald",sans-serif;font-size:15px;text-transform:uppercase;display:flex;align-items:center;justify-content:center;letter-spacing:.3px}

/* hero */
.hero{top:0;height:563px;background:linear-gradient(180deg,#6f7d8c 0%,#8aa0ad 35%,#5d7c86 55%,#a98a6a 78%,#8a6b4e 100%)}
.site-header{position:absolute;top:0;left:0;width:1200px;height:82px}
.brand{position:absolute;left:76px;top:18px;display:flex;align-items:center;gap:12px;color:var(--white);font-family:"Oswald",sans-serif;font-size:20px}
.brand-dot{width:42px;height:42px;border-radius:50%;background:var(--white)}
.nav{position:absolute;left:340px;top:33px;display:flex;gap:28px;font-family:"Open Sans",sans-serif;font-size:13px;color:var(--white)}
.nav .current{color:var(--orange)}
.header-phone{position:absolute;right:76px;top:28px;display:flex;align-items:center;gap:10px;color:var(--white);font-size:13px}
.header-phone strong{font-family:"Oswald",sans-serif;font-weight:400;font-size:18px}
.hero-copy{position:absolute;left:150px;top:222px;color:var(--white)}
.hero-copy h1{font-weight:400;font-size:35px;line-height:44px;width:280px}
.hero-copy p{font-size:15px;margin-top:10px}
.hero-arrows{position:absolute;left:152px;top:501px;display:flex;gap:10px}

.donate-form{position:absolute;left:765px;top:128px;width:359px;height:484px;background:var(--navy);z-index:2}
.form-head{height:105px;background:var(--orange);text-align:center;color:#222;position:relative;padding-top:30px}
.form-head h2{font-family:"Oswald",sans-serif;font-weight:400;font-size:25px;line-height:28px}
.form-head p{font-size:14px;font-weight:600;color:var(--white);margin-top:4px}
.form-head:after{content:"";position:absolute;left:172px;bottom:-12px;border:12px solid transparent;border-bottom:0;border-top-color:var(--orange)}
.field{position:absolute;height:37px;background:var(--white);font-size:11px;color:#aaa;display:flex;align-items:center;padding-left:16px}
.field.select:after{content:"";position:absolute;right:14px;top:15px;width:5px;height:5px;border-right:1px solid #aaa;border-bottom:1px solid #aaa;transform:rotate(45deg)}

/* why donate */
.why{top:563px;height:505px;background:var(--grey-bg);text-align:center}
.why .heading{position:absolute;top:106px;width:100%;font-size:29px;color:#222}
.step{position:absolute;top:184px;width:300px;text-align:center}
.step-icon{margin:0 auto;width:84px;height:84px;border-radius:50%;background:var(--icon-fill)}
.step h3{font-weight:400;font-size:18px;margin-top:36px;color:#222}
.step p{font-size:14px;color:var(--muted);line-height:20px;margin-top:6px}
.step a{text-decoration:none}
.link-orange{color:var(--orange)}
.link-navy{color:var(--navy)}

/* about */
.about{top:1068px;height:446px;background:var(--white)}
.about-photo{position:absolute;left:229px;top:59px;width:282px;height:322px;background:linear-gradient(180deg,#5e93c4 0%,#8fb5d6 40%,#7b7a62 70%,#5b5a48 100%)}
.about-copy{position:absolute;left:612px;top:78px;width:360px}
.about-copy h2{font-size:25px;color:#222}
.about-copy .lead{font-size:15px;color:#777;line-height:21px;margin-top:20px}
.about-copy h4{font-size:12px;font-weight:600;color:#222;margin-top:22px}
.about-copy .note{font-size:12px;color:#555;line-height:20px;margin-top:2px;width:335px}

/* faq */
.faq{top:1514px;height:588px;background:linear-gradient(180deg,#33449e 0%,var(--navy) 50%,#27378d 100%)}
.faq .heading{position:absolute;top:56px;width:100%;text-align:center;font-size:30px;color:var(--white)}
.faq-list{position:absolute;left:229px;top:119px;width:741px;list-style:none;border-top:1px solid rgba(255,255,255,.3)}
.faq-item{border-bottom:1px solid rgba(255,255,255,.3);color:var(--white);padding:0 28px;position:relative}
.faq-q{height:49px;display:flex;align-items:center;font-size:14px}
.faq-toggle{position:absolute;right:18px;top:17px;width:15px;height:15px;border-radius:50%;background:rgba(255,255,255,.8)}
.faq-toggle:before,.faq-toggle.plus:after{content:"";position:absolute;background:var(--navy)}
.faq-toggle:before{left:3px;top:6.5px;width:9px;height:2px}
.faq-toggle.plus:after{left:6.5px;top:3px;width:2px;height:9px}
.faq-a{font-size:11.5px;line-height:19px;padding:0 0 14px;margin-top:-6px}

/* footer */
.site-footer{top:2102px;height:185px;background:linear-gradient(160deg,#f4f4f6 0%,#eceef2 40%,#f1e9ea 70%,#eef0f4 100%)}
.footer-call{position:absolute;left:153px;top:64px;font-size:20px;color:#555}
.footer-call span{color:var(--orange);font-family:"Oswald",sans-serif}
.copyright{position:absolute;left:153px;top:110px;font-size:12px;color:#777}
.social{position:absolute;left:869px;top:62px;display:flex;gap:9px}
.social span{width:30px;height:30px;border-radius:50%;background:#b7b9c2}
.social span.active{background:var(--orange)}
.footer-nav{position:absolute;right:153px;top:110px;font-size:12px;color:#666;display:flex;gap:14px}
.footer-nav i{font-style:normal;color:#aaa}
</style>
</head>
<body>

<section class="section hero" role="img" aria-label="Photo of a white center-console boat pulled up on a sandy beach by the sea">
  <header class="site-header">
    <div class="brand"><span class="brand-dot"></span>Anchorwell Giving</div>
    <nav class="nav">
      <span class="current">Our Story</span><span>Why Donate</span><span>FAQ's</span><span>Contact US</span>
    </nav>
    <div class="header-phone">Call Today to Donate
      <svg width="24" height="24" viewBox="0 0 24 24"><circle cx="12" cy="12" r="11" fill="none" stroke="#f26b4a" stroke-width="1.6"/><path d="M8 6.5l2 0 1 3-1.5 1a7 7 0 0 0 4 4l1-1.5 3 1v2a1.5 1.5 0 0 1-1.5 1.5A10 10 0 0 1 6.5 8 1.5 1.5 0 0 1 8 6.5z" fill="#f26b4a"/></svg>
      <strong>1-800-555-0199</strong>
    </div>
  </header>
  <div class="hero-copy">
    <h1>Donate Boat to Charity!</h1>
    <p>Your car can make a difference!</p>
  </div>
  <div class="hero-arrows">
    <svg width="24" height="24" viewBox="0 0 24 24"><circle cx="12" cy="12" r="10.5" fill="none" stroke="#fff" stroke-width="1.6"/><path d="M13.5 7.5L9 12l4.5 4.5" fill="none" stroke="#fff" stroke-width="1.8"/></svg>
    <svg width="24" height="24" viewBox="0 0 24 24"><circle cx="12" cy="12" r="10.5" fill="none" stroke="#fff" stroke-width="1.6"/><path d="M10.5 7.5L15 12l-4.5 4.5" fill="none" stroke="#fff" stroke-width="1.8"/></svg>
  </div>
</section>

<form class="donate-form">
  <div class="form-head">
    <h2>DONATE YOUR BOAT!</h2>
    <p>Full Tax Deduction - Running or Not</p>
  </div>
  <div class="field" style="left:32px;top:138px;width:295px">Name</div>
  <div class="field" style="left:32px;top:187px;width:142px">Phone</div>
  <div class="field select" style="left:185px;top:187px;width:142px">Zip Code</div>
  <div class="field" style="left:32px;top:236px;width:295px">Email</div>
  <div class="field" style="left:32px;top:286px;width:295px">Model of Boat</div>
  <div class="field select" style="left:32px;top:335px;width:142px">Year</div>
  <div class="field select" style="left:185px;top:335px;width:142px">Make</div>
  <div class="btn" style="left:32px;top:395px;width:295px;height:40px">Submit Application</div>
</form>

<section class="section why">
  <h2 class="heading">Why Donate <span class="accent">Your Boat to Us</span></h2>
  <div class="step" style="left:94px">
    <div class="step-icon" role="img" aria-label="Illustration of a letter and a phone for contacting the charity"></div>
    <h3>Call Or Fill Form</h3>
    <p>Call us at <a class="link-orange">1-888-555-0142</a> or Fill out<br>the <a class="link-navy">online form</a></p>
  </div>
  <div class="step" style="left:450px">
    <div class="step-icon" role="img" aria-label="Illustration of a boat ready for towing"></div>
    <h3>We Tow Boat Free</h3>
    <p>Donate you boat &amp; arrange for easy<br>pick-up and free towing.</p>
  </div>
  <div class="step" style="left:805px">
    <div class="step-icon" role="img" aria-label="Illustration of tax receipt papers"></div>
    <h3>Tax Write Off</h3>
    <p>You will receive your tax deductible<br>vehicle donation receipt.</p>
  </div>
  <div class="btn" style="left:534px;top:399px;width:132px;height:41px">Donate Now</div>
</section>

<section class="section about">
  <div class="about-photo" role="img" aria-label="Photo of soldiers in uniform marching with an American flag against a blue sky"></div>
  <div class="about-copy">
    <h2 class="heading">About <span class="accent">Anchorwell Giving</span></h2>
    <p class="lead">An IRS 501(c)3 nonprofit organization.<br>Boat donations help fund programs and benefit<br>Harbor Service Fund.</p>
    <h4>Schedule a Free Pickup:</h4>
    <p class="note">Complete the form and a representative will call you to<br>arrange a convenient time to pickup your car.</p>
  </div>
  <div class="btn" style="left:612px;top:317px;width:132px;height:39px">Our Story</div>
</section>

<section class="section faq" role="img" aria-label="Faded photo of soldiers in the field under a navy blue overlay">
  <h2 class="heading">Frequently Asked <span class="accent">Questions</span></h2>
  <ul class="faq-list">
    <li class="faq-item"><div class="faq-q">What type of vehicles can be donated?</div><span class="faq-toggle plus"></span></li>
    <li class="faq-item"><div class="faq-q">What paperwork do I need to donate my vehicle?</div><span class="faq-toggle"></span>
      <p class="faq-a">All you need is a title, free of all leins. We will request some general information from you at the time of donation such as, the year, make, and model of the car, as well as its general mechanical condition. We accept all vehicles, running or non-running.</p></li>
    <li class="faq-item"><div class="faq-q">Is my donated vehicle tax-deductible?</div><span class="faq-toggle plus"></span></li>
    <li class="faq-item"><div class="faq-q">What if the vehicle is not registered in my name?</div><span class="faq-toggle plus"></span></li>
    <li class="faq-item"><div class="faq-q">How much will I receive as a tax deduction for my vehicle?</div><span class="faq-toggle plus"></span></li>
    <li class="faq-item"><div class="faq-q">When will I receive my tax receipt?</div><span class="faq-toggle plus"></span></li>
    <li class="faq-item"><div class="faq-q">How do I schedule a pick up?</div><span class="faq-toggle plus"></span></li>
  </ul>
</section>

<footer class="section site-footer" role="img" aria-label="Faded American flag background">
  <p class="footer-call">Call Today to Donate! <span>1-888-555-0142</span> or <span>Email Us</span></p>
  <p class="copyright">© 2017 Anchorwell Giving. All Rights Reserved.</p>
  <div class="social"><span class="active"></span><span></span><span></span><span></span><span></span></div>
  <nav class="footer-nav"><span>Our Story</span><i>|</i><span>Why Donate</span><i>|</i><span>FAQ's</span><i>|</i><span>Contact US</span></nav>
</footer>

</body>
</html>
```